Realtor business card

Looking for a business card that will stand out from the rest. My area of expertise is residential real estate and loans.

Industry/Entity Type

Residential

Requirements
Must have
• Owen Blakely, SFR
Broker
Mortgage Loan Originator
Notary Public
DRE License #07392518
NMLS 581637
Cell 714-529-4170
Fax 888-415-2967
www.owenblakely-example.com
ob@owenblakely-example.com

```html
<!DOCTYPE html>
<html lang="en">
<head>
<meta charset="utf-8">
<title>Owen Blakely — Business Card</title>
<link rel="stylesheet" href="https://fonts.googleapis.com/css2?family=Open+Sans:wght@400;600&display=swap">
<style>
  :root {
    --card-bg: #ffffff;
    --ink: #000000;
    --accent-corner: #000000;
  }
  html, body {
    margin: 0;
    padding: 0;
    width: 1200px;
    height: 695px;
    overflow: hidden;
    background: var(--card-bg);
  }
  .card {
    position: relative;
    width: 1200px;
    height: 695px;
    background: var(--card-bg);
    overflow: hidden;
    font-family: "Open Sans", Arial, sans-serif;
    color: var(--ink);
  }
  .identity {
    position: absolute;
    left: 0;
    right: 0;
    top: 66px;
    margin: 0;
    text-align: center;
  }
  .identity .name {
    margin: 0;
    font-size: 36px;
    font-weight: 600;
    line-height: 46px;
    letter-spacing: -0.3px;
  }
  .identity .titles {
    margin: 0;
    font-size: 21px;
    font-weight: 400;
    line-height: 32px;
  }
  .contact-block {
    position: absolute;
    left: 0;
    right: 0;
    top: 208px;
    margin: 0;
    padding: 0;
    list-style: none;
    text-align: center;
    font-weight: 400;
    font-size: 34px;
    line-height: 46.5px;
    letter-spacing: -0.3px;
  }
  .corner-accent {
    position: absolute;
    right: 0;
    bottom: 0;
    width: 247px;
    height: 276px;
  }
  .corner-accent polygon {
    fill: var(--accent-corner);
  }
</style>
</head>
<body>
  <main class="card">
    <header class="identity">
      <h1 class="name">Owen Blakely, SFR</h1>
      <p class="titles">Broker · Mortgage Loan Originator · Notary Public</p>
    </header>
    <ul class="contact-block">
      <li class="license">DRE License #07392518</li>
      <li class="nmls">NMLS 581637</li>
      <li class="cell">Cell 714-529-4170</li>
      <li class="fax">Fax 888-415-2967</li>
      <li class="website">www.owenblakely-example.com</li>
      <li class="email">ob@owenblakely-example.com</li>
    </ul>
    <svg class="corner-accent" viewBox="0 0 247 276" aria-hidden="true">
      <polygon points="247,0 247,276 0,276"/>
    </svg>
  </main>
</body>
</html>
```